Business Card for Coastal Bedrock Consulting

We need a business card for Coastal Bedrock Consulting. The company website address is provided below. The company logo is attached. We provide specialized permafrost services to the mining, transportation, and oil & gas industries. The card should be prepared for:
Randall Whitacre, PhD.
Coastal Bedrock Consulting
PO Box 418539
Moose Hollow, Alaska 99642
Direct: +1-907-555-0143
Email: rwhitacre@bedrockadvisory.example
Website: www.coastalbedrockconsulting.example

```html
<!DOCTYPE html>
<html lang="en">
<head>
<meta charset="utf-8">
<title>Coastal Bedrock Consulting — Business Card</title>
<link href="https://fonts.googleapis.com/css2?family=Montserrat:wght@400;600;700&display=swap" rel="stylesheet">
<style>
  :root {
    --navy: #111a24;
    --ink: #1b2530;
    --paper: #ffffff;
    --backdrop: #e9e6e1;
    --shadow: rgba(0, 0, 0, 0.18);
  }
  * { box-sizing: border-box; margin: 0; padding: 0; }
  html, body {
    width: 1200px;
    height: 900px;
    overflow: hidden;
    background: var(--backdrop);
    font-family: "Montserrat", sans-serif;
  }
  .stage {
    width: 1200px;
    height: 900px;
    display: flex;
    flex-direction: column;
    align-items: center;
    justify-content: center;
    gap: 56px;
  }
  .card {
    width: 588px;
    height: 336px;
    border-radius: 4px;
    box-shadow: 0 10px 28px var(--shadow);
    display: flex;
    flex-direction: column;
    align-items: center;
    justify-content: center;
    text-align: center;
  }
  .card--front { background: var(--navy); color: var(--paper); }
  .card--back { background: var(--paper); color: var(--ink); }

  .wordmark {
    font-weight: 600;
    text-transform: uppercase;
    letter-spacing: 0.22em;
    line-height: 1.25;
  }
  .card--front .wordmark { font-size: 34px; }
  .card--back .wordmark { font-size: 20px; margin-bottom: 14px; }

  .holder-name { font-size: 21px; font-weight: 700; }
  .holder-company { font-size: 14px; font-weight: 400; margin-top: 2px; }

  .icon-row { display: flex; gap: 6px; justify-content: center; margin: 8px 0 4px; }
  .icon {
    width: 22px; height: 22px; border-radius: 50%;
    background: var(--ink);
    display: flex; align-items: center; justify-content: center;
  }
  .icon svg { width: 13px; height: 13px; }
  .pin svg { width: 20px; height: 24px; }

  .address, .contact { font-size: 13.5px; line-height: 1.35; }
</style>
</head>
<body>
  <main class="stage">
    <section class="card card--front" aria-label="Card front">
      <div class="wordmark">Coastal Bedrock<br>Consulting</div>
    </section>

    <section class="card card--back" aria-label="Card back">
      <div class="wordmark">Coastal Bedrock Consulting</div>
      <div class="holder-name">Randall Whitacre, PhD</div>
      <div class="holder-company">Coastal Bedrock Consulting</div>

      <div class="icon-row pin" aria-hidden="true">
        <svg viewBox="0 0 20 24"><path d="M10 0a9 9 0 0 0-9 9c0 6.5 9 15 9 15s9-8.5 9-15a9 9 0 0 0-9-9z" fill="var(--ink)"/><circle cx="10" cy="9" r="3.4" fill="var(--paper)"/></svg>
      </div>
      <div class="address">Coastal Bedrock Consulting<br>PO Box 418539</div>

      <div class="icon-row" aria-hidden="true">
        <span class="icon"><svg viewBox="0 0 16 16"><path d="M3.5 1.5l2.5 2.8-1.4 1.8a9 9 0 0 0 5.3 5.3l1.8-1.4 2.8 2.5-1.5 2C7.5 14.5 1.5 8.5 1.5 3z" fill="var(--paper)"/></svg></span>
        <span class="icon"><svg viewBox="0 0 16 16"><rect x="1.5" y="3.5" width="13" height="9" rx="1" fill="none" stroke="var(--paper)" stroke-width="1.6"/><path d="M2 4.2l6 4.6 6-4.6" fill="none" stroke="var(--paper)" stroke-width="1.6"/></svg></span>
        <span class="icon"><svg viewBox="0 0 16 16"><circle cx="8" cy="8" r="6.2" fill="none" stroke="var(--paper)" stroke-width="1.5"/><ellipse cx="8" cy="8" rx="2.6" ry="6.2" fill="none" stroke="var(--paper)" stroke-width="1.2"/><path d="M2 8h12" stroke="var(--paper)" stroke-width="1.2"/></svg></span>
      </div>
      <div class="contact">
        +1-907-555-0143<br>
        rwhitacre@bedrockadvisory.example<br>
        www.coastalbedrockconsulting.example
      </div>
    </section>
  </main>
</body>
</html>
```